Video Streaming Website Design Needed

We are a non-profit organization and currently have a website called LumenVerseHub.org
We want to launch a new version of the site that will look completely different. It is a video streaming site. We have the programmers who will work on it but we just need a designer.
We have an idea of what we want the layout to be. You can check out samples of the idea we have for the rough layout.
http://lumenversehub.org/images/LV_2.0_Homepage2.jpg
http://lumenversehub.org/images/LV_2.0_Video_Page.jpg
http://lumenversehub.org/images/LV_2.0_Individual_Speakers_Page.jpg
http://lumenversehub.org/images/LV_2.0_Registration_Page.jpg
Those are just some of our pages we plan on having.
This is a Jewish site and we have holidays through out the year and we would like to incorporate sort of a theme for each holiday using a background design change. For example, this site http://media.qpr7.layoutdepot.example/xk_48190/index.html , has a nice background and maybe we can use a similar idea to change the theme of the background depending on the holiday.
Target Market(s)
Jews and spiritual minded people. Men & Women. Ages 16-55.
Industry/Entity Type
Non-Profit
Look and feel
Each slider illustrates characteristics of the customer's brand and the style your logo design should communicate.

```html
<!DOCTYPE html>
<html lang="en">
<head>
<meta charset="utf-8">
<title>LumenVerseHub.org</title>
<link href="https://fonts.googleapis.com/css2?family=Arimo:wght@400;700&display=swap" rel="stylesheet">
<style>
:root{
  --bg-deep:#1f4fb0;
  --bg-light:#8fc0ec;
  --brand:#1049c8;
  --brand-dark:#0b3aa8;
  --sky:#3fa9e8;
  --link:#2c9be0;
  --ink:#333;
  --ink-soft:#666;
  --panel:#e4e6e9;
  --panel-edge:#d2d5d9;
  --row-alt:#dfe4f0;
  --white:#fff;
}
*{box-sizing:border-box;margin:0;padding:0}
html,body{width:1200px;height:952px;overflow:hidden}
body{font-family:"Arimo",Arial,sans-serif;color:var(--ink);position:relative}
.backdrop{position:absolute;inset:0;background:linear-gradient(100deg,var(--bg-deep) 0%,#3c78cf 45%,var(--bg-light) 100%)}
.page{position:absolute;left:204px;top:59px;width:795px;height:828px;background:var(--white);border-radius:6px;box-shadow:0 2px 10px rgba(0,0,0,.25)}
.abs{position:absolute}
.brand{left:14px;top:26px;display:flex;align-items:center;gap:8px}
.brand-dot{width:38px;height:38px;border-radius:50%;background:var(--brand)}
.brand-name{font-size:30px;font-weight:400;color:var(--brand);letter-spacing:-.5px}
.dateline{right:125px;top:9px;text-align:right;font-size:10px;color:#555;line-height:16px}
.dateline a{color:var(--brand);text-decoration:none}
.dateline .muted{color:#888}
.donate{left:681px;top:0;width:103px;height:37px;background:linear-gradient(#2a6ee0,var(--brand-dark));color:#fff;font-size:16px;font-weight:700;display:flex;align-items:center;justify-content:center;border-radius:0 0 4px 4px;letter-spacing:-.3px}
.donate span{color:#7cc8ff;font-weight:400}
.nav{left:9px;top:92px;width:777px;height:41px;background:linear-gradient(#5cb8f2,#1a66d6 55%,#1057c9);border-radius:3px}
.nav ul{list-style:none;display:flex;gap:21px;position:absolute;left:20px;top:13px}
.nav li{color:#fff;font-size:11.5px;font-weight:700}
.search{left:521px;top:8px;width:249px;height:25px;background:#fff;border-radius:3px;display:flex;align-items:center}
.search svg{margin:0 6px}
.search .field{flex:1;font-size:10.5px;color:#444;border-left:1px solid #ddd;padding-left:7px;height:17px;line-height:17px}
.search .go{width:64px;height:23px;margin-right:1px;background:linear-gradient(#3d8fe6,#1452c7);color:#fff;font-size:11.5px;font-weight:700;display:flex;align-items:center;justify-content:center;border-radius:2px}
.hero{left:9px;top:140px;width:513px;height:306px;border-radius:4px;overflow:hidden;background:#e9eaec}
.hero-photo{height:231px;background:radial-gradient(circle at 45% 45%,#d9a88a 0%,#a86d55 35%,#6c4434 70%,#3b2a25 100%)}
.hero-label{left:15px;top:8px;color:#fff;font-size:12px;font-weight:700}
.hero-caption{position:absolute;left:14px;top:238px;font-size:10.5px;line-height:13.4px;color:#123a8c}
.hero-caption h2{font-size:15.5px;color:var(--brand);margin-bottom:2px}
.latest{left:530px;top:141px;width:256px;height:306px;background:#f4f5f7;border-radius:3px;overflow:hidden}
.tabs{display:flex;height:34px;background:var(--brand)}
.tabs div{color:#fff;font-size:10.5px;font-weight:700;display:flex;align-items:center;justify-content:center;border-left:1px solid #4d86e0;background:linear-gradient(#3c8ae6,#165ad0)}
.tabs .on{background:#e2e4e8;color:#222;border:none}
.rows{list-style:none;width:243px}
.rows li{height:38.7px;padding:7px 8px 0 7px;font-size:9.5px;position:relative}
.rows li:nth-child(even){background:var(--row-alt)}
.rows b{color:#333}
.rows .who{display:block;padding-left:11px;color:#555;margin-top:3px}
.rows .when{position:absolute;right:7px;top:7px;font-weight:700}
.scroll{position:absolute;right:2px;top:36px;width:9px;height:268px;border-left:1px solid #ccc}
.scroll i{position:absolute;left:1px;top:34px;width:7px;height:58px;border:1px solid #bbb;border-radius:4px;background:#fafafa}
.card{background:linear-gradient(#f0f1f3,var(--panel));border-radius:4px;border-bottom:2px solid var(--panel-edge)}
.card h3{font-size:17px;font-weight:400;color:var(--link);letter-spacing:-.4px}
.stats{left:9px;top:454px;width:513px;height:157px}
.stats h3{position:absolute;left:15px;top:12px}
.chart{position:absolute;left:27px;top:46px}
.stat-col{position:absolute;top:50px;list-style:none;font-size:12.5px;line-height:23.2px}
.stat-col b{display:inline-block;width:24px;text-align:right;margin-right:10px;font-weight:400;color:#555;font-size:15px}
.stat-col span{color:var(--link)}
.login{left:530px;top:454px;width:256px;height:157px}
.login h3{position:absolute;left:12px;top:10px}
.login label{position:absolute;left:12px;font-size:10px;font-weight:700;color:#555;letter-spacing:.3px}
.login .input{position:absolute;left:82px;width:200px;max-width:166px;height:24px;background:#fff;border:1px solid #e0e0d0;border-radius:3px}
.login .opts{position:absolute;left:73px;top:124px;font-size:9.5px;color:#333;display:flex;gap:12px;align-items:center;top:121px}
.login .opts i{display:inline-block;width:9px;height:9px;border:1px solid #777;margin-left:6px;vertical-align:-1px}
.btn{position:absolute;top:149px;height:27px;color:#fff;font-size:12.5px;display:flex;align-items:center;justify-content:center;border-radius:2px}
.btn.join{left:8px;width:180px;background:linear-gradient(#7fd0f7,#3fb0ec);top:149px}
.btn.enter{left:195px;width:55px;background:linear-gradient(#3d8fe6,#1452c7);font-weight:700}
.partners{left:9px;top:620px;width:777px;height:107px;background:linear-gradient(#e6e7e9,#f1f2f3);border-radius:4px}
.partners p{position:absolute;left:14px;top:12px;font-size:11.5px;font-weight:700;color:#999}
.marks{position:absolute;left:22px;top:44px;display:flex;align-items:center;gap:30px}
.mark{background:#b8b8b8;border-radius:3px}
.foot{left:0;width:795px;top:749px;text-align:center;font-size:9.6px;line-height:14px;color:#777}
.foot strong{display:block;color:#123a8c;font-size:10px;margin-bottom:6px}
</style>
</head>
<body>
<div class="backdrop" role="img" aria-label="Blue toned photo backdrop of a man in a prayer shawl sounding a ram's horn"></div>
<main class="page">
  <div class="abs brand"><span class="brand-dot"></span><span class="brand-name">LumenVerseHub</span></div>
  <div class="abs dateline">Wednesday May 18 2011 - Lyar 14, 5771<br><a>Join Now</a> <span class="muted">| Login</span></div>
  <div class="abs donate">Donate<span>Now</span></div>

  <nav class="abs nav">
    <ul><li>About Torah</li><li>Videos</li><li>Speakers</li><li>Jewish Links</li><li>Contact Us</li><li>Privacy &amp; Terms</li></ul>
    <div class="abs search">
      <svg width="16" height="16" viewBox="0 0 16 16"><circle cx="6.5" cy="6.5" r="5" fill="none" stroke="#999" stroke-width="1.5"/><line x1="10.2" y1="10.2" x2="14.5" y2="14.5" stroke="#999" stroke-width="1.8"/></svg>
      <div class="field">Search</div>
      <div class="go">Search</div>
    </div>
  </nav>

  <section class="abs hero">
    <div class="hero-photo" role="img" aria-label="Photo of a bearded lecturer in glasses speaking into a microphone"></div>
    <div class="abs hero-label">UPCOMING LECTURES &amp; EVENTS</div>
    <div class="hero-caption">
      <h2>Saturday Night</h2>
      LumenVerseHub Video Presentation - Saturday Nights at 8:30pm<br>
      Free pizza will be served!<br>
      Location : Beit Orah Community Hall - 41-20 Maple Avenue, Glenview 11402
    </div>
  </section>

  <section class="abs latest">
    <div class="tabs">
      <div class="on" style="width:68px">Latest</div>
      <div style="width:104px">Bookmarks</div>
      <div style="width:60px">Tags</div>
      <div style="width:62px">Random</div>
    </div>
    <ol class="rows">
      <li><b>1. FaceLink is Evil</b><span class="when">10.09.2011</span><span class="who">R. Eliyahu Marden</span></li>
      <li><b>2. I Don't work in the auto industry</b><span class="when">10.09.2011</span><span class="who">R. Natan Kolber</span></li>
      <li><b>3. Your Mistaking me for the singer</b><span class="when">10.09.2011</span><span class="who">R. Avi Senderov</span></li>
      <li><b>4. Your All Going to Hell!</b><span class="when">10.09.2011</span><span class="who">R. Eliyahu Marden</span></li>
      <li><b>5. That will be 50% Off</b><span class="when">10.09.2011</span><span class="who">R. Eliyahu Marden</span></li>
      <li><b>6. FaceLink is Evil</b><span class="when">10.09.2011</span><span class="who">R. Eliyahu Marden</span></li>
      <li><b>7. I Don't work in the auto industry</b><span class="when">10.09.2011</span><span class="who">R. Eliyahu Marden</span></li>
    </ol>
    <div class="scroll"><i></i></div>
  </section>

  <section class="abs card stats">
    <h3>Site Statistics</h3>
    <svg class="chart" width="96" height="96" viewBox="0 0 96 96">
      <polygon points="2,82 70,70 94,78 28,92" fill="#9aa0a8"/>
      <rect x="22" y="36" width="10" height="46" fill="#8a9099"/>
      <rect x="34" y="30" width="10" height="50" fill="#2f7fe0"/>
      <rect x="46" y="22" width="10" height="56" fill="#2f7fe0"/>
      <rect x="58" y="12" width="10" height="64" fill="#1c5fcf"/>
      <rect x="70" y="4" width="10" height="70" fill="#6e7580"/>
    </svg>
    <ul class="stat-col" style="left:165px">
      <li><b>1</b><span>Videos Added Today</span></li>
      <li><b>12</b><span>Videos Added This Week</span></li>
      <li><b>15</b><span>Videos Added This Month</span></li>
      <li><b>42</b><span>Added This Year</span></li>
    </ul>
    <ul class="stat-col" style="left:370px">
      <li><b style="width:38px">203</b><span>Members</span></li>
      <li><b style="width:38px">12</b><span>Online</span></li>
      <li><b style="width:38px">4</b><span>Events</span></li>
      <li><b style="width:38px">152</b><span>Catagories</span></li>
    </ul>
  </section>

  <section class="abs card login">
    <h3>Member Login</h3>
    <label style="top:51px">USERNAME</label><div class="input" style="top:43px"></div>
    <label style="top:82px">PASSWORD</label><div class="input" style="top:74px"></div>
    <div class="opts"><span>Forget Password</span><span>Remember Me<i></i></span></div>
    <div class="btn join" style="top:121px">Join LumenVerseHub Now</div>
    <div class="btn enter" style="top:121px">Login</div>
  </section>

  <section class="abs partners">
    <p>All of the learning today on LumenVerseHub.org is dedicated to:</p>
    <div class="marks">
      <div class="mark" style="width:120px;height:30px"></div>
      <div class="mark" style="width:130px;height:30px"></div>
      <div class="mark" style="width:64px;height:52px"></div>
      <div class="mark" style="width:170px;height:22px"></div>
      <div class="mark" style="width:120px;height:26px"></div>
    </div>
  </section>

  <footer class="abs foot">
    <strong>© Copyright LumenVerseHub.org 2007 - 2011. All Rights Reserved.</strong>
    The content on LumenVerseHub.org and related sites is for personal use only. It may not be distributed,<br>
    duplicated, broadcasted or otherwise reproduced in any way, shape or form without express written<br>
    permission from us. For permission to show content publicly, please contact us at hello@lumenversehub.org
  </footer>
</main>
</body>
</html>
```